Business cards and Stationary | Corvel Music Events

Hello! We need business cards and stationery for a new small business in the music industry. "Corvel is a high-end music agency which provides an unparalleled level of talent and personalized service to the realm entertainment, corporate events, and luxury weddings. Here is where the classical meets the contemporary and we can bring your vision to life.Keeping a steady finger on the pulse of current trends and consistently raising the bar for industry standards, Corvel continues to rise to the forefront of the music industry, providing the utmost professional, high-end, elegant, and engaging entertainment in Australia and World-Wide."

Target Market(s)

Class A. high profile corporate business.

Industry/Entity Type

Entertainment

Contact Information for Business Card

Corvel Music Events

Tessa Holloway
Director | Violinist

Level 7, 41 Marlow Street
Sydney, 2000

Website: www.corvelmusicevents.com
Phone number: 0481 352 604
Email: tessa@corvelmusicevents.com

Font styles to use
Serif
Sans Serif
Script

Colors
feeeee
0355a3
f59296
ffffff

Requirements
Nice to have
• Clean and sophisticated would be perfect.
• If there is a way to include the Instagram without being tacky, that would be awesome
• @corvelmusicevents
• Our website and logo have the following fonts:
• The primary logo is inspired and based on a font called BillionScript but the B is completely hand drawn and the rest is customised a bit to work together cohesively
• Monserrat Light - Is the Music part of the logo and as headers in the site
• Open Sans 300 and 400 (Light or Regular) is used mostly as the body text in the site
• If you want to access the website:
• www.corvelmusicevents.com
• username: client
• password: preview

```html
<!DOCTYPE html>
<html lang="en">
<head>
<meta charset="utf-8">
<title>Corvel Music Events — Business Card</title>
<link rel="stylesheet" href="https://fonts.googleapis.com/css2?family=Open+Sans:wght@300;400&display=swap">
<style>
  :root {
    --backdrop: #ebc3a6;
    --bronze: #9c6551;
    --band: #b38a7c;
    --veil: #ffffff;
    --photo-light: #e9e6e4;
    --photo-mid: #b9b4b2;
    --photo-warm: #7a4330;
    --ink-soft: #8a6656;
    --card-shadow: rgba(120, 70, 40, 0.25);
  }
  html, body {
    margin: 0;
    width: 1200px;
    height: 856px;
    overflow: hidden;
    background: var(--backdrop);
  }
  .stage {
    position: relative;
    width: 1200px;
    height: 856px;
    display: flex;
    align-items: center;
    justify-content: center;
    gap: 60px;
  }
  .card {
    width: 530px;
    height: 303px;
    border-radius: 22px;
    overflow: hidden;
    box-shadow: 0 14px 30px var(--card-shadow);
    font-family: "Open Sans", sans-serif;
  }
  .card svg { display: block; }
  .brand-name { font-family: "Open Sans", sans-serif; font-weight: 300; fill: var(--bronze); }
  .web-line { font-family: "Open Sans", sans-serif; font-weight: 400; fill: var(--bronze); }
  .contact-line { font-family: "Open Sans", sans-serif; font-weight: 300; fill: var(--ink-soft); font-size: 12.5px; }
  .holder-name { font-family: "Open Sans", sans-serif; font-weight: 300; fill: var(--veil); font-size: 13px; }
  .contact-icon { fill: none; stroke: var(--ink-soft); stroke-width: 1.2; }
</style>
</head>
<body>
<main class="stage">

  <!-- Front of card -->
  <section class="card card-front">
    <svg width="530" height="303" viewBox="0 0 530 303">
      <defs>
        <linearGradient id="frontPhoto" x1="0" y1="1" x2="1" y2="0">
          <stop offset="0" stop-color="var(--photo-mid)"/>
          <stop offset="0.45" stop-color="var(--photo-light)"/>
          <stop offset="0.75" stop-color="#c9a594"/>
          <stop offset="1" stop-color="var(--photo-light)"/>
        </linearGradient>
      </defs>
      <rect class="photo-area" width="530" height="303" fill="url(#frontPhoto)" role="img" aria-label="Soft-focus photograph of a violinist's hands playing a violin"/>
      <path class="accent-band" d="M0,58 C150,40 300,120 430,303 L372,303 C270,160 140,98 0,100 Z" fill="var(--band)" opacity="0.9"/>
      <path class="veil-swoosh" d="M0,58 C200,-10 420,8 530,55 L530,303 L430,303 C300,120 150,40 0,58 Z" fill="var(--veil)" opacity="0.82"/>
      <path class="veil-edge" d="M0,58 C200,-10 420,8 530,55" fill="none" stroke="var(--veil)" stroke-width="2" opacity="0.9"/>
      <g class="brand-mark">
        <circle cx="176" cy="128" r="6" fill="var(--bronze)"/>
        <text class="brand-name" x="192" y="139" font-size="32">Corvel Music</text>
      </g>
      <text class="web-line" x="505" y="270" font-size="15" text-anchor="end">www.corvelmusicevents.com</text>
    </svg>
  </section>

  <!-- Back of card -->
  <section class="card card-back">
    <svg width="530" height="303" viewBox="0 0 530 303">
      <defs>
        <linearGradient id="backPhoto" x1="0" y1="1" x2="1" y2="0">
          <stop offset="0" stop-color="#d8cfc6"/>
          <stop offset="0.3" stop-color="var(--photo-warm)"/>
          <stop offset="0.55" stop-color="#e8e2dc"/>
          <stop offset="1" stop-color="#b0603a"/>
        </linearGradient>
      </defs>
      <rect class="photo-area" width="530" height="303" fill="url(#backPhoto)" role="img" aria-label="Close-up photograph of a violin scroll resting on a woven cloth"/>
      <path class="veil-swoosh" d="M0,45 C190,5 400,-5 530,10 L530,303 L270,303 C300,200 150,95 0,98 Z" fill="var(--veil)" opacity="0.86"/>
      <path class="veil-edge" d="M0,45 C190,5 400,-5 530,10" fill="none" stroke="var(--veil)" stroke-width="2"/>
      <g class="brand-mark">
        <circle cx="174" cy="56" r="5" fill="var(--bronze)"/>
        <text class="brand-name" x="188" y="65" font-size="26">Corvel Music</text>
      </g>
      <g class="contact-list">
        <g transform="translate(292,108)">
          <path class="contact-icon" d="M0,-5 a4,4 0 0 1 8,0 c0,3 -4,8 -4,8 c0,0 -4,-5 -4,-8 z"/>
          <text class="contact-line" x="16" y="0">Level 7, 41 Marlow Street,</text>
          <text class="contact-line" x="16" y="16">Sydney, 2000</text>
        </g>
        <g transform="translate(292,140)">
          <rect class="contact-icon" x="0" y="-8" width="8" height="10" rx="1.5"/>
          <text class="contact-line" x="16" y="0">0481 352 604</text>
        </g>
        <g transform="translate(292,160)">
          <circle class="contact-icon" cx="4" cy="-3" r="4.5"/>
          <text class="contact-line" x="16" y="0">0481 352 604</text>
        </g>
        <g transform="translate(292,180)">
          <rect class="contact-icon" x="-0.5" y="-8" width="9" height="7"/>
          <path class="contact-icon" d="M-0.5,-8 L4,-4 L8.5,-8"/>
          <text class="contact-line" x="16" y="0">contact@corvelmusicevents.com</text>
        </g>
        <g transform="translate(292,200)">
          <circle class="contact-icon" cx="4" cy="-3" r="4.5"/>
          <path class="contact-icon" d="M-0.5,-3 H8.5 M4,-7.5 V1.5"/>
          <text class="contact-line" x="16" y="0">www.corvelmusicevents.com</text>
        </g>
      </g>
      <g class="card-holder">
        <text class="holder-name" x="40" y="262">Example Name</text>
        <text class="holder-name" x="40" y="279">Founder</text>
      </g>
    </svg>
  </section>

</main>
</body>
</html>
```